Web Design Project

8 page static website.
About us/What we stand for:
Forno Lucente CBD plans to make a huge splash in Sydney by being the first Italian pizza and pasta retail food outlet offering truly fresh, nutritious ingredients – herbs and vegetables are picked directly from the garden, pizzas are made with love in a fun filled atmosphere and a cutting edge brand strategy that promotes a happy lifestyle and reminds people that happiness and togetherness comes from sharing amazing food.
The best thing about Forno Lucente is that it offers consumers a choice to either choose from the enticing gluten free and vegetarian menu range to the more traditional pizza and pasta, we cater for their own tastes, this provides a distinct point of difference in the retail food market, as well as allowing consumers to have an endless range of choices without having to worry about the nutritional value.
Consumers have now become accustomed to a consistent brand experience which is setting increasingly high standards when it comes to food quality, taste and service.
We want to capitalise on the opportunity to create a strong, modern brand that promotes healthy lifestyle habits, sells fresh, wholesome ingredients, delivers
exceptional service in a fun filled atmosphere and appeals to a broad market.
Our business model is specifically pickup and delivery with a few seats and crates for eating in. It is for the time poor that still want to have a great tasting Italian experience with pizza and pasta within the quick service restaurant space. Takeaway, office catering and delivery will be a large percentage of our business.
Our philosophy at Forno Lucente is simple:
“Success is not a formula, it’s a recipe”.
Brand personality:
We are located in a laneway and basically the shop is a hole in the one. It looks like a restaurant you would see in Italy.
Modern Italian, contemporary, fun, rustic (Taco Vela, Brasa’s)
1 Aims of this website
• Emotionally connect with the target audience to reflect (“happiness and togetherness comes from sharing amazing food”)
• To entice people to order pizza
• To capture a mailing list
• To differentiate us from the low cost, low quality pizza
• To create a connection with the target audience, and promote word of mouth
2 Target audience(s)
• Male/Female
• 18-49
• Sydney CBD and Woolloomooloo
• Internet Savvy.
3. Contents/Functionality
www.crustwagon.com.au – like the rustic brown in the website and the old washed out white colour through the font.
Target Market(s)
18-49 years old
City worker and resident
people that enjoy good food
Industry/Entity Type
Restaurant
Requirements
Must have
- Some splash of red and green to represent the italian theme.
Attached is a draft of the homepage layout.
Attached below are some fonts that we like.
Nice to have
- Please see http://www.brasashop.com.au/Pages/locationmenu.aspx
This is how our takeaway menu looks like.

```html
<!DOCTYPE html>
<html lang="en">
<head>
<meta charset="utf-8">
<title>Forno Lucente – Home</title>
<link rel="stylesheet" href="https://fonts.googleapis.com/css2?family=Bebas+Neue&family=Handlee&family=Arimo:wght@400&family=Fredoka:wght@600&display=swap">
<style>
:root{
  --brick:#9c2f30;
  --brick-dark:#8d2728;
  --cream:#ebe1bf;
  --cream-text:#f1dfb4;
  --green:#1f8a32;
  --charcoal:#3c3c3c;
  --field:#c9c9c9;
  --red:#a3302f;
  --mustard:#e0c23a;
  --white:#ffffff;
  --ink:#333333;
  --cloth-light:#efd3d5;
  --cloth-dark:#e4a9ae;
}
*{margin:0;padding:0;box-sizing:border-box}
html,body{width:1200px;height:1000px;overflow:hidden}
body{position:relative;background:radial-gradient(ellipse at 50% 40%,#a53637 0%,var(--brick) 55%,var(--brick-dark) 100%);font-family:"Arimo",Arial,sans-serif;color:var(--ink)}
.abs{position:absolute}
.display{font-family:"Bebas Neue",Impact,sans-serif;letter-spacing:.3px}

/* header */
.brand{left:172px;top:13px;width:188px;height:188px;border-radius:50%;background:var(--green);display:flex;align-items:center;justify-content:center;z-index:3}
.brand span{font-family:"Fredoka",sans-serif;font-weight:600;color:var(--white);font-size:34px;line-height:1.05;text-align:center}
.follow{right:264px;top:35px;color:var(--white);font-size:21px}
.social{top:24px;width:33px;height:33px;border-radius:50%}
.social.one{left:953px;background:#2a3fa8}
.social.two{left:1000px;background:#25b4d8}
.nav{left:368px;top:68px;display:flex;align-items:flex-end;height:52px}
.nav a{font-family:"Bebas Neue",Impact,sans-serif;font-size:29px;color:var(--cream-text);text-decoration:none;padding:6px 6px 10px;border-right:1px dotted rgba(241,223,180,.6);line-height:1}
.nav a:last-child{border-right:0}
.nav a.current{background:var(--green);color:var(--white);border-radius:12px 12px 0 0;padding:10px 10px 14px;border-right:0;margin-right:8px}
.phone{left:776px;top:64px;color:var(--white);white-space:nowrap}
.phone small{font-size:29px;margin-right:4px}
.phone b{font-weight:400;font-size:36px}
.phone strong{font-weight:400;font-size:52px;margin-left:12px;letter-spacing:1px}
.rule{left:368px;top:119px;width:670px;height:3px;background:var(--green)}

/* banner */
.banner-photo{left:160px;top:122px;width:285px;height:272px;background:linear-gradient(160deg,#6d3a22 0%,#b7552e 45%,#d9c2a0 75%,#7a4a2c 100%);border-top-left-radius:6px}
.banner-promo{left:445px;top:122px;width:593px;height:272px;background:linear-gradient(135deg,var(--cloth-light) 0%,var(--cloth-dark) 100%);border-top-right-radius:6px;text-align:center}
.promo-title{font-family:"Handlee",cursive;font-size:57px;color:#3a3a3a;margin-top:24px;line-height:1;padding-left:20px}
.promo-sub{font-family:"Bebas Neue",Impact,sans-serif;font-size:31px;color:#3a3a3a;margin-top:20px;padding-left:12px}

/* content panel */
.panel{left:160px;top:394px;width:878px;height:335px;background:var(--cream);border-radius:0 0 10px 10px}
.order-head{left:195px;top:421px;font-size:23px;font-weight:400;color:var(--ink);letter-spacing:0}
.order-head em{font-style:normal;color:var(--red)}
.login{left:178px;top:467px;width:386px;height:213px;background:var(--charcoal);border-radius:10px}
.login-head{left:198px;top:484px;color:var(--white);font-size:23px;display:flex;align-items:center;gap:10px;letter-spacing:0}
.login-head svg{margin-left:10px}
.field{left:197px;width:326px;height:32px;border-radius:8px;background:var(--field);font-size:17px;color:#333;padding:6px 0 0 17px}
.forgot{left:213px;top:617px;color:#ddd;font-size:14.5px}
.logon{left:428px;top:606px;width:95px;height:35px;border-radius:8px;background:var(--red);color:var(--white);font-size:26px;text-align:center;line-height:37px}
.info h3{font-family:"Bebas Neue",Impact,sans-serif;font-weight:400;font-size:24px;color:var(--red);display:flex;align-items:center;gap:10px;margin-left:-2px}
.info p{font-size:14.2px;line-height:17.5px;color:#333;margin-top:14px;width:200px}
.info a{font-size:14.2px;color:var(--red);text-decoration:underline}

/* footer */
.download{left:166px;top:692px;width:188px;height:190px}
.hours h3,.find h3{font-family:"Bebas Neue",Impact,sans-serif;font-weight:400;font-size:29px;color:var(--cream-text)}
.hours p,.find p{color:var(--white);font-size:12px;line-height:16.5px;margin-top:4px}
.map{left:612px;top:744px;width:215px;height:98px;border-radius:10px;background:linear-gradient(135deg,#c2686a,#b04a4c)}
</style>
</head>
<body>

<header>
  <div class="abs brand"><span>Forno<br>Lucente</span></div>
  <div class="abs follow display">Follow us:</div>
  <span class="abs social one" aria-label="Social link"></span>
  <span class="abs social two" aria-label="Social link"></span>
  <nav class="abs nav">
    <a class="current" href="#">Home</a><a href="#">Menu</a><a href="#">About us</a><a href="#">Contact us</a>
  </nav>
  <div class="abs phone display"><small>PH</small><b>02</b><strong>9555 0142</strong></div>
  <div class="abs rule"></div>
</header>

<section>
  <div class="abs banner-photo" role="img" aria-label="Photo of grilled bread and fresh tomatoes on a wooden board"></div>
  <div class="abs banner-promo" role="img" aria-label="Checked tablecloth with a drawn place setting of plate, fork and knife">
    <p class="promo-title">2 for 1 sharing plates</p>
    <p class="promo-sub">Every Wednesday &amp; Thursday in December</p>
  </div>
</section>

<main>
  <div class="abs panel"></div>
  <h2 class="abs order-head display"><em>Order online</em> - earn slices &amp; free pizzas</h2>

  <div class="abs login"></div>
  <div class="abs login-head display">
    <span>Log on to order online</span><span>|</span>
    <svg width="32" height="32" viewBox="0 0 32 32" aria-hidden="true"><circle cx="16" cy="16" r="16" fill="#fff"/><path d="M16 16 L1 16 A15 15 0 0 1 6 5 Z" fill="#1f8a32"/></svg>
    <span>Register</span>
  </div>
  <div class="abs field" style="top:525px">User ID</div>
  <div class="abs field" style="top:565px">Password</div>
  <div class="abs forgot">Forgot password?</div>
  <div class="abs logon display">Log on</div>

  <article class="abs info" style="left:616px;top:418px">
    <h3><svg width="32" height="32" viewBox="0 0 32 32" aria-hidden="true"><circle cx="16" cy="16" r="16" fill="#fff"/><path d="M16 16 L1 16 A15 15 0 0 1 6 5 Z" fill="#1f8a32"/></svg>Delivery area</h3>
    <p>Lorem ipsum dolor sit amet, consectetuer adipiscing elit, sed diam nonummy nibh euis-mod tincidunt ut laoreet dolore magna aliquam erat volutpat.</p>
    <a href="#">Read more &gt;</a>
  </article>
  <article class="abs info" style="left:825px;top:418px">
    <h3><svg width="32" height="32" viewBox="0 0 32 32" aria-hidden="true"><circle cx="16" cy="16" r="16" fill="#fff"/><path d="M16 16 L1 16 A15 15 0 0 1 6 5 Z" fill="#1f8a32"/></svg>Office catering</h3>
    <p style="margin-left:-2px">Lorem ipsum dolor sit amet, consectetuer adipiscing elit, sed diam nonummy nibh euis-mod tincidunt ut laoreet dolore magna aliquam erat volutpat.</p>
    <a href="#" style="margin-left:-2px">Read more &gt;</a>
  </article>
</main>

<footer>
  <svg class="abs download" viewBox="0 0 188 190" aria-label="Download a menu">
    <circle cx="94" cy="95" r="94" fill="#e0c23a"/>
    <path d="M94 95 L64 4 A94 94 0 0 1 134 10 Z" fill="#a3302f"/>
    <text x="92" y="100" text-anchor="middle" font-family="Fredoka, sans-serif" font-weight="600" font-size="26" fill="#fff" letter-spacing="1.5">DOWNLOAD</text>
    <text x="102" y="137" text-anchor="middle" font-family="Fredoka, sans-serif" font-weight="600" font-size="26" fill="#fff" letter-spacing="1.5">A MENU</text>
  </svg>

  <div class="abs hours" style="left:370px;top:738px">
    <h3>Opening hours</h3>
    <p>Monday to Wednesday 7:30am – 9pm<br>Thursday &amp; Friday 7:30am – 10:30pm<br>Saturday 8am - 9pm<br>Sunday 10am - 6pm</p>
  </div>

  <div class="abs map" role="img" aria-label="Street map showing the shop location"></div>
  <svg class="abs" style="left:750px;top:748px" width="30" height="40" viewBox="0 0 30 40" aria-hidden="true">
    <path d="M15 39 C15 39 2 22 2 14 A13 13 0 0 1 28 14 C28 22 15 39 15 39 Z" fill="#b01e22" stroke="#7a1214" stroke-width="1.5"/>
    <circle cx="15" cy="14" r="5" fill="#d9494b"/>
  </svg>

  <div class="abs find" style="left:847px;top:738px">
    <h3>Where to find us</h3>
    <p>24 Vesta Lane, Sydney<br>NSW, 2000, Australia<br>On the corner of<br>Vesta &amp; Marlow Streets</p>
  </div>
</footer>

</body>
</html>
```